Sticker label for natural moisturizer

I need a sticker label designed for a homemade moisturizer made from beef tallow and honey.
Must include: Logo, product name (Classic Suet & Clover Salve), ingredients (in English and Polish, can use placeholder text for initial design), brief description of product with instructions for use (in English and Polish, can use placeholder text for initial design), manufacturer name (vorelmart.com), manufacturer address (placeholder text for initial design), volume of container (60ml / 2oz)
The product is used by both males and females of all ages, so must be unisex design with broad appeal.
Dimensions: Length 15cm, Height 3cm
Style: Has to simultaneously communicate that this is a homemade product with no chemical fillers AND that it is of extremely high quality.
Brand colors:
#57665C
#FCFAF6
#FFFFFF
#000000
#B99B83
#EAE4DD
#CC8E5A

```html
<!DOCTYPE html>
<html lang="en">
<head>
<meta charset="utf-8">
<title>Classic Suet &amp; Clover Salve – Jar Label</title>
<link rel="stylesheet" href="https://fonts.googleapis.com/css2?family=Montserrat:wght@500;700&family=Cormorant+Garamond:wght@500&display=swap">
<style>
  :root {
    --backdrop: #e4e4e4;
    --sage: #57665C;
    --sage-deep: #2c3a31;
    --paper: #FFFFFF;
    --cream: #FCFAF6;
    --ink: #1a1a1a;
    --gold: #E9A928;
    --gold-deep: #d98f12;
    --line: #d8d2ca;
  }
  * { box-sizing: border-box; margin: 0; padding: 0; }
  html, body { width: 1200px; height: 839px; overflow: hidden; }
  body {
    background: var(--backdrop);
    font-family: "Montserrat", sans-serif;
    position: relative;
  }
  .label {
    position: absolute;
    left: 50px; top: 309px;
    width: 1100px; height: 220px;
    display: flex;
    box-shadow: 0 6px 24px rgba(0,0,0,.12);
  }
  .info-panel {
    width: 200px;
    background: var(--cream);
    padding: 16px 14px;
    display: flex;
    flex-direction: column;
    gap: 7px;
    color: var(--ink);
  }
  .info-block { border-left: 3px solid var(--gold); padding-left: 7px; }
  .info-heading { font-size: 8px; font-weight: 700; letter-spacing: .04em; }
  .info-text { font-size: 7.5px; font-weight: 500; line-height: 1.3; }
  .maker { margin-top: auto; font-size: 7.5px; font-weight: 500; line-height: 1.35; }
  .maker strong { font-weight: 700; }

  .front-panel {
    flex: 1;
    position: relative;
    background: linear-gradient(120deg, #7d8b81 0%, var(--sage) 40%, var(--sage-deep) 100%);
    display: flex;
    flex-direction: column;
    align-items: center;
    padding-top: 14px;
  }
  .brand-name {
    font-family: "Montserrat", sans-serif;
    font-weight: 700;
    font-size: 52px;
    line-height: 1;
    color: var(--paper);
    letter-spacing: .01em;
  }
  .product-name {
    font-family: "Cormorant Garamond", serif;
    font-weight: 500;
    font-size: 38px;
    color: var(--gold);
    margin-top: 4px;
    line-height: 1;
  }
  .feature-row {
    display: flex;
    align-items: center;
    gap: 22px;
    margin-top: 14px;
  }
  .feature-art {
    width: 40px; height: 38px;
    border-radius: 6px;
    background: rgba(255,255,255,.75);
  }
  .feature-badge { display: block; }
  .divider { width: 1px; height: 30px; background: rgba(255,255,255,.6); }
  .volume-tab {
    position: absolute;
    bottom: 0; left: 50%;
    transform: translateX(-50%);
    width: 180px; height: 30px;
    background: linear-gradient(90deg, var(--gold), var(--gold-deep));
    display: flex; align-items: center; justify-content: center;
    font-family: "Cormorant Garamond", serif;
    font-size: 20px;
    color: var(--ink);
  }
</style>
</head>
<body>
  <section class="label">
    <aside class="info-panel info-panel--left">
      <div class="info-block">
        <p class="info-heading">DESCRIPTION</p>
        <p class="info-text">Rich whipped salve for daily care.</p>
      </div>
      <div class="info-block">
        <p class="info-heading">OPIS</p>
        <p class="info-text">Bogaty balsam do codziennej pielęgnacji.</p>
      </div>
      <div class="info-block">
        <p class="info-heading">DIRECTIONS</p>
        <p class="info-text">Warm a little between fingers and apply.</p>
      </div>
      <div class="info-block">
        <p class="info-heading">STOSOWANIE</p>
        <p class="info-text">Rozgrzej w dłoniach i nałóż na skórę.</p>
      </div>
      <p class="maker"><strong>vorelmart.com</strong><br>12 Placeholder Street, 00-000 City</p>
    </aside>

    <div class="front-panel">
      <h1 class="brand-name">vorel</h1>
      <h2 class="product-name">Classic Suet &amp; Clover Salve</h2>
      <div class="feature-row">
        <div class="feature-art" role="img" aria-label="Line icon of a cow head"></div>
        <span class="divider"></span>
        <div class="feature-art" role="img" aria-label="Line icon of a honeycomb with a honey dipper"></div>
        <span class="divider"></span>
        <svg class="feature-badge" width="40" height="40" viewBox="0 0 40 40" aria-hidden="true">
          <polygon points="20,2 36,11 36,29 20,38 4,29 4,11" fill="#FFFFFF"/>
        </svg>
      </div>
      <div class="volume-tab">60 ml / 2 oz</div>
    </div>

    <aside class="info-panel info-panel--right">
      <div class="info-block">
        <p class="info-heading">INGREDIENTS</p>
        <p class="info-text">Beef suet, raw honey, olive oil.</p>
      </div>
      <div class="info-block">
        <p class="info-heading">SKŁADNIKI</p>
        <p class="info-text">Łój wołowy, miód, oliwa.</p>
      </div>
      <div class="info-block">
        <p class="info-heading">WARNING</p>
        <p class="info-text">External use only.</p>
      </div>
      <div class="info-block">
        <p class="info-heading">OSTRZEŻENIE</p>
        <p class="info-text">Tylko do użytku zewnętrznego.</p>
      </div>
    </aside>
  </section>
</body>
</html>
```